I'm a magician . hypnotist also a good barber. I need this all to be shown in good detail on the cards.

Industry/Entity Type

Magician

Contact Information for Business Card

Magician/ hypnotist/barber Rowan Pitt. One of the best. Tel 07421 736204
Email.Trickshears48@fernmail.example
Title of card spell chap.

```html
<!DOCTYPE html>
<html lang="en">
<head>
<meta charset="utf-8">
<title>Spell Chap – Business Card</title>
<link rel="stylesheet" href="https://fonts.googleapis.com/css2?family=Jost:wght@400;500&display=swap">
<style>
  :root {
    --backdrop: #1a1a1a;
    --card-teal: #0b5c60;
    --art-light: #2f7f83;
    --art-dark: #0a2e31;
    --ink-white: #ffffff;
    --bar-text: #0b5c60;
  }
  * { margin: 0; padding: 0; box-sizing: border-box; }
  html, body {
    width: 1200px;
    height: 1200px;
    overflow: hidden;
    background: var(--backdrop);
    font-family: "Jost", sans-serif;
  }
  .business-card {
    position: absolute;
    left: 100px;
    top: 277px;
    width: 1000px;
    height: 646px;
    background: var(--card-teal);
    color: var(--ink-white);
  }
  .brand-name {
    position: absolute;
    left: 60px;
    top: 72px;
    width: 380px;
    text-align: center;
    font-size: 52px;
    font-weight: 500;
    letter-spacing: 4px;
    text-transform: uppercase;
    color: var(--ink-white);
    line-height: 1;
  }
  .brand-artwork {
    position: absolute;
    left: 80px;
    top: 150px;
    width: 410px;
    height: 250px;
    border-radius: 125px 40px 40px 125px;
    background: radial-gradient(circle at 38% 45%, var(--art-light) 0%, var(--card-teal) 55%, var(--art-dark) 100%);
  }
  .name-bar {
    position: absolute;
    left: 520px;
    top: 150px;
    right: 0;
    height: 70px;
    background: var(--ink-white);
    display: flex;
    align-items: center;
    padding-left: 34px;
  }
  .person-name {
    font-size: 44px;
    font-weight: 400;
    letter-spacing: 1px;
    text-transform: uppercase;
    color: var(--bar-text);
  }
  .tagline {
    position: absolute;
    left: 545px;
    top: 265px;
    font-size: 38px;
    font-weight: 400;
    text-transform: uppercase;
    letter-spacing: 1px;
  }
  .services {
    position: absolute;
    right: 95px;
    top: 360px;
    list-style: none;
    text-align: right;
    font-size: 36px;
    line-height: 48px;
    text-transform: uppercase;
    letter-spacing: 1px;
  }
  .contact {
    position: absolute;
    top: 540px;
    display: flex;
    align-items: center;
    gap: 16px;
    font-size: 30px;
  }
  .contact-phone { left: 40px; }
  .contact-email { left: 360px; }
  .contact-icon { fill: var(--ink-white); }
</style>
</head>
<body>
  <main class="business-card">
    <p class="brand-name">Spell Chap</p>

    <div class="brand-artwork" role="img" aria-label="Illustration of a white swirl with barber scissors and a magician's top hat with wand"></div>

    <div class="name-bar">
      <h1 class="person-name">Rowan Pitt</h1>
    </div>

    <p class="tagline">One of the best</p>

    <ul class="services">
      <li>Magician</li>
      <li>Hypnotist</li>
      <li>Barber</li>
    </ul>

    <p class="contact contact-phone">
      <svg class="contact-icon" width="26" height="36" viewBox="0 0 26 36" aria-hidden="true">
        <path d="M6 1 L11 1 L12 10 L8 12 C9 18 12 23 16 26 L19 23 L25 27 L23 33 C20 36 14 35 9 29 C3 21 0 12 3 4 Z"/>
      </svg>
      07421 736204
    </p>

    <p class="contact contact-email">
      <svg class="contact-icon" width="42" height="28" viewBox="0 0 42 28" aria-hidden="true">
        <path d="M0 0 H42 V28 H0 Z M3 3 L21 17 L39 3 Z" fill-rule="evenodd"/>
      </svg>
      Trickshears48@fernmail.example
    </p>
  </main>
</body>
</html>
```